Business Card Design Project : Ferncliff Media

In preparation for market launch, Whistler's Ferncliff Media require the development of a business card. Ferncliff Media is a Community online publishing web portal. We provide the the city of Whistler located in B.C. (Canada) business directories, News, Classified ads, News, Events and blogs etc.

The main focus of the brand is to help local businesses to corporate with their online advertisement and marketing. Meeting our clients face to face is a must (B2B).

Target Market(s)

The target market is B2B customers. Business Owners to Marketing, advertising Managers

Industry/Entity Type

Business

Requirements
Must have
• - The business card will be two sided.
the BACK side will have our logo which consist of (icon, url,slogan) submited. The logo will be middle and centred.

The FRONT side should have company details:

Company Legal Name: TALLPINE FERNCLIFF MEDIA

Dale Morrow
Director of Sales & Marketing

www.tallpineferncliff.biz
dale@tallpineferncliff.biz

Phone: 604 555 0138
#2217 - 581 E. Harlow Ave.
Vancouver, B.C. V6N2K4 Canada
Nice to have
• - For the "FRONT" side of our business card. You can separate or re-arrange with our logo components (icon, logo,slogan). It does not have to be together.

Also our company legal name is rather long so arrange or organize the name in a way to make it shorter. Your experience and creativity will have to come in play.
Should not have
• should not have other colors beside logo color and black text (2 colors). Also nothing Three dimensional

```html
<!DOCTYPE html>
<html lang="en">
<head>
<meta charset="utf-8">
<title>Tallpine Ferncliff Media – Business Card</title>
<link rel="stylesheet" href="https://fonts.googleapis.com/css2?family=Source+Sans+3:wght@400;600;700&display=swap">
<style>
  :root {
    --brand-blue: #2179c1;
    --ink: #111111;
    --paper: #ffffff;
    --stage: #e9e9e7;
  }
  * { box-sizing: border-box; margin: 0; padding: 0; }
  html, body { width: 1200px; height: 900px; overflow: hidden; }
  body {
    position: relative;
    background: var(--stage);
    font-family: "Source Sans 3", "Myriad Pro", Arial, sans-serif;
    color: var(--ink);
  }
  .card {
    position: absolute;
    width: 587px;
    height: 380px;
    background: var(--paper);
    overflow: hidden;
  }
  .card--front { left: 93px; top: 48px; }
  .card--back  { left: 471px; top: 466px; }

  .brand-dot {
    position: absolute;
    left: 50%;
    width: 56px;
    height: 56px;
    margin-left: -28px;
    border-radius: 50%;
    background: var(--brand-blue);
  }
  .card--front .brand-dot { top: 44px; }
  .card--back .brand-dot { top: 104px; }

  .company-name {
    position: absolute;
    left: 0; right: 0;
    text-align: center;
    font-weight: 700;
    color: var(--ink);
    letter-spacing: -0.2px;
    white-space: nowrap;
  }
  .tagline {
    position: absolute;
    left: 0; right: 0;
    text-align: center;
    font-weight: 400;
    color: var(--brand-blue);
  }
  .card--front .company-name { top: 108px; font-size: 21px; }
  .card--front .tagline { top: 137px; font-size: 18px; }
  .card--back .company-name { top: 184px; font-size: 23px; }
  .card--back .tagline { top: 216px; font-size: 20px; }

  .contact-list {
    position: absolute;
    left: 42px;
    top: 196px;
    list-style: none;
    font-size: 14.5px;
    line-height: 19px;
  }
  .contact-item {
    display: flex;
    align-items: flex-start;
    margin-bottom: 5.5px;
  }
  .contact-icon {
    flex: none;
    width: 14px;
    height: 14px;
    margin-top: 2px;
    margin-right: 9px;
    fill: var(--brand-blue);
  }

  .person {
    position: absolute;
    right: 36px;
    top: 219px;
    text-align: right;
  }
  .person-name {
    font-size: 19px;
    font-weight: 700;
    color: var(--brand-blue);
    line-height: 24px;
  }
  .person-title {
    font-size: 15px;
    font-weight: 600;
    line-height: 20px;
  }

  .card-waves {
    position: absolute;
    left: 0; top: 0;
    width: 587px;
    height: 380px;
  }
  .wave--black { fill: var(--ink); }
  .wave--blue { fill: var(--brand-blue); }

  .card-url {
    position: absolute;
    left: 0; right: 0;
    top: 336px;
    text-align: center;
    font-size: 15.5px;
    color: var(--brand-blue);
  }
</style>
</head>
<body>

<section class="card card--front" aria-label="Business card front">
  <span class="brand-dot" aria-hidden="true"></span>
  <h1 class="company-name">TALLPINE FERNCLIFF MEDIA</h1>
  <p class="tagline">Your information gateway</p>

  <ul class="contact-list">
    <li class="contact-item">
      <svg class="contact-icon" viewBox="0 0 14 14" aria-hidden="true"><path d="M7 1 L13.5 7 H11.5 V13 H8.5 V9 H5.5 V13 H2.5 V7 H0.5 Z"/></svg>
      <span>#2217 - 581 E. Harlow Ave.<br>Vancouver, B.C. V6N2K4 Canada</span>
    </li>
    <li class="contact-item">
      <svg class="contact-icon" viewBox="0 0 14 14" aria-hidden="true"><path d="M3 1 L5.5 1 L6.3 4.2 L4.8 5.6 C5.6 7.4 6.6 8.4 8.4 9.2 L9.8 7.7 L13 8.5 L13 11 C13 12.2 12 13 10.8 12.9 C5.8 12.4 1.6 8.2 1.1 3.2 C1 2 1.8 1 3 1 Z"/></svg>
      <span>604 555 0138</span>
    </li>
    <li class="contact-item">
      <svg class="contact-icon" viewBox="0 0 14 14" aria-hidden="true"><path d="M1 3 H13 L7 7.5 Z M1 4.5 L7 9 L13 4.5 V11 H1 Z"/></svg>
      <span>dale@tallpineferncliff.biz</span>
    </li>
    <li class="contact-item">
      <svg class="contact-icon" viewBox="0 0 14 14" aria-hidden="true"><circle cx="7" cy="7" r="6"/><path d="M4 4 Q6 3 7 5 Q6 7 4 6.5 Z M8 8 Q10 7.5 10.5 9.5 Q9 11.5 8 10.5 Z" fill="#ffffff"/></svg>
      <span>www.tallpineferncliff.biz</span>
    </li>
  </ul>

  <div class="person">
    <p class="person-name">DALE MORROW</p>
    <p class="person-title">Director of Sales &amp; Marketing</p>
  </div>

  <svg class="card-waves" viewBox="0 0 587 380" aria-hidden="true">
    <path class="wave--black" d="M0,322 C120,326 280,336 365,345 C260,351 120,346 0,338 Z"/>
    <path class="wave--blue" d="M0,352 C150,362 300,360 420,346 C480,339 540,332 587,334 L587,380 L0,380 Z"/>
  </svg>
</section>

<section class="card card--back" aria-label="Business card back">
  <span class="brand-dot" aria-hidden="true"></span>
  <h2 class="company-name">TALLPINE FERNCLIFF MEDIA</h2>
  <p class="tagline">Your information gateway</p>
  <p class="card-url">www.tallpineferncliff.biz</p>
</section>

</body>
</html>
```